New company looking for logo, for business cards and email signature.
we provide Safety, Training and Project Management Services to Mining and Transport sectors.

HALVORN CONSULTANCY, Tom Ashcrove, Principal Consultant, 0491362817, halvornconsultancy@postvale.example , Unit 412,KestwickRidge Business Hub,817 Tulloch Road, Mackay, 4832.
Sustainable Production through Safety, Training and Leadership.

```html
<!DOCTYPE html>
<html lang="en">
<head>
<meta charset="utf-8">
<title>Halvorn Consultancy – Business Card</title>
<link href="https://fonts.googleapis.com/css2?family=Questrial&family=Arimo:wght@700&display=swap" rel="stylesheet">
<style>
  :root {
    --card-black: #0c1113;
    --artwork-glow: #2a2e30;
    --brand-yellow: #e3d300;
    --text-yellow: #dccb00;
  }
  html, body {
    margin: 0;
    padding: 0;
    width: 1200px;
    height: 741px;
    overflow: hidden;
    background: var(--card-black);
  }
  .business-card {
    position: relative;
    width: 1200px;
    height: 741px;
    background: var(--card-black);
    overflow: hidden;
  }
  .artwork-area {
    position: absolute;
    left: 0;
    top: 80px;
    width: 760px;
    height: 560px;
    background: radial-gradient(ellipse 55% 50% at 55% 50%, var(--artwork-glow) 0%, var(--card-black) 100%);
  }
  .brand-name {
    position: absolute;
    margin: 0;
    color: var(--brand-yellow);
    font-family: "Questrial", sans-serif;
    font-weight: 400;
    line-height: 1;
    text-transform: uppercase;
    white-space: nowrap;
  }
  .brand-name__primary {
    left: 180px;
    top: 172px;
    font-size: 132px;
    letter-spacing: 2px;
  }
  .brand-name__secondary {
    left: 174px;
    top: 340px;
    font-size: 72px;
    letter-spacing: 3px;
  }
  .contact-block {
    position: absolute;
    right: 87px;
    top: 418px;
    text-align: right;
    color: var(--text-yellow);
    font-family: "Questrial", sans-serif;
    line-height: 1;
  }
  .contact-block p { margin: 0; white-space: nowrap; }
  .contact-role { font-size: 39px; }
  .contact-name { font-size: 39px; margin-top: 2px !important; padding-right: 10px; }
  .contact-phone { font-size: 30px; margin-top: 12px !important; letter-spacing: 1px; }
  .contact-email { font-size: 36px; margin-top: 8px !important; }
  .office-address {
    position: absolute;
    left: 89px;
    top: 624px;
    margin: 0;
    color: var(--text-yellow);
    font-family: "Arimo", sans-serif;
    font-weight: 700;
    font-size: 26px;
    white-space: nowrap;
  }
</style>
</head>
<body>
  <main class="business-card">
    <div class="artwork-area" role="img" aria-label="Photograph of a curving asphalt road with a double yellow centre line"></div>

    <h1 class="brand-name brand-name__primary">Halvorn</h1>
    <p class="brand-name brand-name__secondary">Consultancy</p>

    <section class="contact-block">
      <p class="contact-role">Principal Consultant</p>
      <p class="contact-name">Tom Ashcrove</p>
      <p class="contact-phone">0491362817</p>
      <p class="contact-email">halvornconsultancy@postvale.example</p>
    </section>

    <p class="office-address">Unit 412 ,KestwickRidge Business Hub,817 Tulloch Road , Mackay, 4832.</p>
  </main>
</body>
</html>
```